Advanced Therapeutic Massage Therapist

I need a business card advertising my massage services as an advanced therapeutic massage therapist. I offer advanced therapeutic massage, swedish and deep tissue. I want to create a simple, professional and feminine card. I like bright colours and creativity.

I prefer a bold and experimental approach rather than something status-quo. A card to suggest therapeutic healing through dynamic massage. Motifs, shapes or layout which suggest movement and flow.

Target Market(s)

Everybody!

Industry/Entity Type

Health And Wellness

Contact Information for Business Card

The card should include:
My name, logo, services offered and my contact details.

Siobhán Delaney
Massage Therapist

- Swedish - Deep Tissue - Advanced Therapeutic

Phone: (+353) 87 296 1740
Email: regenerate@siobhandelaney-example.com
Website: www.siobhandelany-example.com

Font styles to use
Serif
Sans Serif
Decorative
Script

Colors

Designer to choose colors to be used in the design.

Requirements
Must have
• An example may contain something like this, yet concise:
• "Siobhán Delaney
• Massage Therapist
• - Swedish - Deep Tissue - Advanced Therapeutic"
Nice to have
• This sentence is optional:
• Imagery such as a logo or symbol. I have attached a file containing a logo I had produced however the name is incorrect now as it is "Siobhán" not "Sadie". It could be edited to change it to Siobhán.
• I have sent the file as .psd .jpg. .pdf and .png
• I like when the card conveys energy, movement, pressure points, flow etc.
• I just like the designer to follow their own style and ideas. I like bright colours but must have a lot of a base colour to offset it. I really prefer them to follow their own inspiration. That is my preference.
Should not have
• Pine trees, non-native trees to Britain and Ireland, exotic flowers or animals that are not native to Britain and Ireland.
• I don't like brown as the background colour of the card.
• The cars shouldn't look like a wedding invitation i.e too many floral type designs.

```html
<!DOCTYPE html>
<html lang="en">
<head>
<meta charset="utf-8">
<title>Siobhán Delaney – Massage Therapist Business Card</title>
<link rel="stylesheet" href="https://fonts.googleapis.com/css2?family=Kaushan+Script&family=Source+Sans+3:wght@400;600&display=swap">
<style>
  :root {
    --backdrop: #1e1e1e;
    --card-white: #ffffff;
    --mint: #b3e0d1;
    --mint-light: #c9eadf;
    --mint-deep: #a8d3c5;
    --teal-script: #7fcfbb;
    --ink: #1a1a1a;
    --amber: #c0812f;
    --bark: #7a5228;
    --gold: #c19a4a;
  }
  * { margin: 0; padding: 0; box-sizing: border-box; }
  html, body {
    width: 1200px; height: 900px; overflow: hidden;
    background: var(--backdrop);
    font-family: "Source Sans 3", sans-serif;
  }
  .canvas { position: relative; width: 1200px; height: 900px; }
  .card {
    position: absolute; top: 306px; width: 439px; height: 271px;
    border-radius: 12px; overflow: hidden;
  }
  .card--front { left: 149px; background: var(--card-white); }
  .card--back {
    left: 609px;
    background: linear-gradient(160deg, var(--mint-light) 0%, var(--mint-deep) 100%);
  }
  .brand-mark {
    position: absolute; display: flex; flex-direction: column;
    align-items: center; gap: 5px; width: 130px;
  }
  .card--front .brand-mark { left: 57px; top: 78px; }
  .card--back .brand-mark { left: 155px; top: 76px; }
  .brand-mark__circle { width: 96px; height: 96px; display: block; }
  .brand-mark__name {
    font-size: 12px; font-weight: 600; color: var(--gold);
    white-space: nowrap; line-height: 14px;
  }
  .identity { position: absolute; left: 225px; top: 84px; }
  .identity__name {
    font-family: "Kaushan Script", cursive; font-weight: 400;
    font-size: 21px; color: var(--teal-script); line-height: 1.1;
  }
  .identity__role { font-size: 12.5px; color: var(--ink); margin-top: 1px; }
  .contact { list-style: none; margin-top: 18px; }
  .contact__item {
    display: flex; align-items: center; gap: 5px;
    font-size: 12.5px; color: var(--ink); line-height: 16px;
    white-space: nowrap;
  }
  .contact__icon { width: 10px; height: 10px; flex: none; }
  .services {
    position: absolute; left: 0; bottom: 0; width: 100%; height: 52px;
    background: var(--mint);
    display: flex; justify-content: center; align-items: center; gap: 10px;
    list-style: none; padding-left: 6px;
  }
  .services__item {
    display: flex; align-items: center; gap: 5px;
    font-size: 13px; color: var(--amber);
  }
  .services__item::before {
    content: ""; width: 7px; height: 7px; border-radius: 50%;
    background: var(--amber);
  }
  .tagline {
    position: absolute; left: 0; top: 214px; width: 100%;
    text-align: center; font-size: 13px; line-height: 16px; color: var(--bark);
  }
</style>
</head>
<body>
<main class="canvas">
  <section class="card card--front" aria-label="Business card front">
    <div class="brand-mark">
      <svg class="brand-mark__circle" viewBox="0 0 96 96" role="img" aria-label="Brand emblem">
        <defs>
          <radialGradient id="emblemFill" cx="50%" cy="50%" r="50%">
            <stop offset="0%" stop-color="#d8f0e8"/>
            <stop offset="100%" stop-color="#a6d8c8"/>
          </radialGradient>
        </defs>
        <circle cx="48" cy="48" r="46" fill="url(#emblemFill)"/>
      </svg>
      <span class="brand-mark__name">Siobhán Delaney</span>
    </div>
    <div class="identity">
      <h1 class="identity__name">Siobhán Delaney</h1>
      <p class="identity__role">Massage Therapist</p>
      <ul class="contact">
        <li class="contact__item">
          <svg class="contact__icon" viewBox="0 0 10 10" aria-hidden="true">
            <path d="M2 0.6 L3.6 2.6 L2.7 3.7 Q3.8 5.9 6.2 7.2 L7.3 6.3 L9.4 7.9 L8.3 9.4 Q2.8 8.7 0.6 2 Z" fill="#c0812f"/>
          </svg>
          (+353) 87 296 1740
        </li>
        <li class="contact__item">
          <svg class="contact__icon" viewBox="0 0 10 10" aria-hidden="true">
            <rect x="0.5" y="2" width="9" height="6.5" fill="#c0812f"/>
            <path d="M0.8 2.3 L5 5.6 L9.2 2.3" fill="none" stroke="#fff" stroke-width="0.9"/>
          </svg>
          siobhanmassage@example.ie
        </li>
      </ul>
    </div>
    <ul class="services">
      <li class="services__item">Swedish</li>
      <li class="services__item">Deep Tissue</li>
      <li class="services__item">Advanced Therapeutic</li>
    </ul>
  </section>

  <section class="card card--back" aria-label="Business card back">
    <div class="brand-mark">
      <svg class="brand-mark__circle" viewBox="0 0 96 96" role="img" aria-label="Brand emblem">
        <defs>
          <radialGradient id="emblemFillBack" cx="50%" cy="50%" r="50%">
            <stop offset="0%" stop-color="#dff3ec"/>
            <stop offset="100%" stop-color="#93cdb9"/>
          </radialGradient>
        </defs>
        <circle cx="48" cy="48" r="46" fill="url(#emblemFillBack)"/>
      </svg>
      <span class="brand-mark__name">Siobhán Delaney</span>
    </div>
    <p class="tagline">ATHC qualified specialising in advanced therapeutic and<br>deep tissue massage</p>
  </section>
</main>
</body>
</html>
```